Let's help people Kestrel with better hearing!

I need a business card for my private practice. I am a Dr. of Audiology and focus on hearing and tinnitus (ringing in the ears) treatment. My practice is named "Kestrel Hearing and Tinnitus Solutions". I want to communicate the idea of improved quality of life utilizing a natural color pallet Love the color turquoise as an accent. Want a professional look, while eye catching. I'm open to nontraditional design aesthetic. Something to get excited about and motivate people to improve their lives!

```html
<!DOCTYPE html>
<html lang="en">
<head>
<meta charset="utf-8">
<title>Clear Tone Centre – Business Card</title>
<link href="https://fonts.googleapis.com/css2?family=Questrial&family=Tinos&display=swap" rel="stylesheet">
<style>
  :root {
    --backdrop: #2a2a2a;
    --card-light: #ffffff;
    --card-shade: #e4e4e4;
    --accent-blue: #0a7cc4;
    --accent-blue-soft: #3f9ad6;
    --mark-grey: #6e6e6e;
    --ink: #1c1c1c;
  }
  * { box-sizing: border-box; margin: 0; padding: 0; }
  html, body { width: 1200px; height: 900px; overflow: hidden; }
  body {
    background: var(--backdrop);
    font-family: "Questrial", "Century Gothic", sans-serif;
    position: relative;
  }
  .card {
    position: absolute;
    top: 130px;
    width: 400px;
    height: 640px;
    border-radius: 26px;
    overflow: hidden;
    background: linear-gradient(160deg, var(--card-light) 35%, var(--card-shade) 100%);
    box-shadow: 0 18px 40px rgba(0,0,0,0.55);
  }
  .card--back { left: 150px; }
  .card--front { left: 650px; }
  .card__band {
    position: absolute;
    left: 0; top: 0; bottom: 0;
    width: 34px;
    background: var(--accent-blue);
  }
  .brand {
    display: flex;
    align-items: center;
    gap: 22px;
  }
  .brand__dot {
    width: 54px; height: 54px;
    border-radius: 50%;
    background: var(--accent-blue-soft);
    flex: none;
  }
  .brand__name {
    color: var(--mark-grey);
    font-size: 30px;
    line-height: 1.0;
    letter-spacing: 2px;
    text-transform: uppercase;
  }
  .card--back .brand {
    position: absolute;
    left: 80px; top: 190px;
  }
  .tagline {
    position: absolute;
    left: 34px; right: 0; top: 380px;
    text-align: center;
    font-family: "Tinos", "Times New Roman", serif;
    color: var(--accent-blue-soft);
    font-size: 25px;
    line-height: 1.25;
    letter-spacing: 1px;
    text-transform: uppercase;
  }
  .card--front .brand {
    position: absolute;
    left: 70px; top: 48px;
  }
  .contact {
    position: absolute;
    left: 66px; top: 200px;
    list-style: none;
  }
  .contact__person { margin-bottom: 30px; }
  .contact__name { color: var(--accent-blue); font-size: 27px; }
  .contact__role { color: var(--ink); font-size: 20px; }
  .contact__item { margin-bottom: 34px; }
  .contact__label {
    color: var(--accent-blue);
    font-size: 19px;
    text-transform: uppercase;
    letter-spacing: 0.5px;
  }
  .contact__value { color: var(--ink); font-size: 22px; }
</style>
</head>
<body>
  <section class="card card--back" aria-label="Card back">
    <div class="card__band"></div>
    <div class="brand">
      <span class="brand__dot"></span>
      <span class="brand__name">Clear<br>Tone<br>Centre</span>
    </div>
    <p class="tagline">Kestrel Hearing<br>and<br>Tinnitus Solutions</p>
  </section>

  <section class="card card--front" aria-label="Card front">
    <div class="card__band"></div>
    <div class="brand">
      <span class="brand__dot"></span>
      <span class="brand__name">Clear<br>Tone<br>Centre</span>
    </div>
    <ul class="contact">
      <li class="contact__person">
        <div class="contact__name">Name</div>
        <div class="contact__role">Designation</div>
      </li>
      <li class="contact__item">
        <div class="contact__label">Address</div>
        <div class="contact__value">24 Maple Row, Canada</div>
      </li>
      <li class="contact__item">
        <div class="contact__label">Phone</div>
        <div class="contact__value">+41 00 555 01 27</div>
      </li>
      <li class="contact__item">
        <div class="contact__label">E-mail</div>
        <div class="contact__value">info@cleartonecare.com</div>
      </li>
      <li class="contact__item">
        <div class="contact__label">Website</div>
        <div class="contact__value">www.cleartonecare.com</div>
      </li>
    </ul>
  </section>
</body>
</html>
```